Financial Coaching biz needs modern service presentation menu

We need a PowerPoint presentation document with a modern, easy-to-read layout to share with potential clients.

I have a website under development that can be used as a reference www.brightledgerhub.com.

We'd like the doc to be simple to edit because services and verbiage will likely be modified periodically.

Two logo variations have been included.

Target Market(s)

Gen X, Gen Y, and Millienials

Industry/Entity Type

Financial Planning

Colors
85cae6
cadf82
ffffff
dddddd
cfcfcf
cee9f5

```html
<!DOCTYPE html>
<html lang="en">
<head>
<meta charset="utf-8">
<title>Bright Ledger Hub – Service Menu</title>
<link href="https://fonts.googleapis.com/css2?family=Mulish:wght@400;600;700;800&family=Oswald:wght@600&display=swap" rel="stylesheet">
<style>
  :root{
    --navy:#102b52;
    --navy-deep:#0b1f3e;
    --green:#2db36c;
    --green-dark:#1b6e42;
    --blue:#0f3e7e;
    --blue-dark:#0d336a;
    --red:#e21c3d;
    --red-dark:#b3152f;
    --orange:#f47a20;
    --orange-dark:#cf5d14;
    --sky:#29a9e1;
    --sky-dark:#124c72;
    --card:#dddddd;
    --ink:#1d1d1d;
    --white:#ffffff;
  }
  *{margin:0;padding:0;box-sizing:border-box}
  html,body{width:1200px;height:848px;overflow:hidden;background:var(--navy)}
  .sheet{position:relative;width:1200px;height:848px;overflow:hidden;
    background:radial-gradient(circle at 860px 330px,#2a5d8e 0,#163a66 260px,var(--navy) 520px);
    font-family:"Mulish",sans-serif}
  .stripe{position:absolute;left:0;width:1200px;height:18px;display:flex}
  .stripe.top{top:0}.stripe.bottom{bottom:0;height:20px}
  .stripe span{height:100%}
  .accent-arrow{position:absolute;left:0;top:18px}
  .service{position:absolute;width:173px;height:316px;display:flex;flex-direction:column}
  .service .icon-zone{height:114px;display:flex;align-items:center;justify-content:center}
  .service .icon-zone .disc{width:80px;height:80px;border-radius:50%;display:flex;align-items:center;justify-content:center}
  .service h2{height:44px;display:flex;align-items:center;justify-content:center;text-align:center;
    color:var(--white);font-weight:700;font-size:15px;line-height:1.15}
  .service .body{height:148px;background:var(--card);padding:9px 12px 0 16px;color:var(--ink);
    font-size:11.8px;line-height:1.2;text-align:justify}
  .service .body p+p{margin-top:14px}
  .service .foot{height:10px}
  .brand{position:absolute;left:400px;top:230px;width:220px;text-align:center;color:var(--white);
    font-family:"Oswald",sans-serif;font-weight:600;font-size:44px;line-height:1.05;letter-spacing:1px}
  .brand .dot{display:block;width:30px;height:30px;border-radius:50%;background:#2fbf7a;margin:0 auto 14px}
  .photo{position:absolute;left:560px;top:18px;width:640px;height:442px;
    background:radial-gradient(ellipse at 60% 60%,#4a8fc4 0,#1d4b7d 45%,rgba(16,43,82,0) 75%)}
  .promise{position:absolute;left:572px;top:458px;width:598px;height:306px;background:var(--red);
    border-radius:38px;color:var(--white);font-weight:700;font-size:16px;line-height:1.45;padding:36px 24px 0 20px}
  .promise .seal-room{float:right;width:150px;height:96px;margin-top:-12px}
  .promise p:first-of-type{text-align:justify}
  .promise p+p{margin-top:9px}
  .seal{position:absolute;left:1018px;top:402px}
  .perks{position:absolute;left:19px;top:786px;width:1151px;height:32px;background:var(--navy-deep);
    border-radius:10px;color:var(--white);font-weight:800;font-size:15px;display:flex;align-items:center;justify-content:center}
</style>
</head>
<body>
<div class="sheet">
  <div class="stripe top">
    <span style="width:156px;background:var(--green)"></span><span style="width:162px;background:var(--orange)"></span>
    <span style="width:160px;background:var(--red)"></span><span style="width:136px;background:var(--blue)"></span>
    <span style="width:158px;background:var(--green)"></span><span style="width:160px;background:var(--orange)"></span>
    <span style="width:162px;background:var(--red)"></span><span style="width:106px;background:var(--blue)"></span>
  </div>

  <svg class="accent-arrow" width="160" height="100" viewBox="0 0 160 100">
    <polygon points="0,0 40,0 150,75 120,95 0,30" fill="#1d6b9a"/>
    <polygon points="12,0 28,0 125,72 118,80" fill="#cfe7f1"/>
  </svg>

  <div class="photo" role="img" aria-label="Businessman in a suit examining a holographic data display with a magnifying glass"></div>

  <section class="service" style="left:19px;top:130px">
    <div class="icon-zone" style="background:var(--green)">
      <div class="disc" style="background:var(--green-dark)">
        <svg width="46" height="40" viewBox="0 0 46 40"><rect x="2" y="2" width="42" height="28" rx="2" fill="none" stroke="#fff" stroke-width="3"/><polyline points="9,22 17,14 24,19 36,9" fill="none" stroke="#fff" stroke-width="2.5"/><rect x="19" y="30" width="8" height="5" fill="#fff"/><rect x="13" y="35" width="20" height="3" fill="#fff"/></svg>
      </div>
    </div>
    <h2 style="background:var(--green-dark)">Monetary<br>Action Plan</h2>
    <div class="body"><p>Establish full-year plan for spending and saving, including major purchases or events.</p></div>
    <div class="foot" style="background:var(--green-dark)"></div>
  </section>

  <section class="service" style="left:202px;top:130px">
    <div class="icon-zone" style="background:var(--blue)">
      <div class="disc" style="background:#2fc08a">
        <svg width="30" height="40" viewBox="0 0 30 40"><rect x="2" y="4" width="26" height="34" rx="2" fill="#fff"/><rect x="10" y="1" width="10" height="6" fill="#ddd"/><rect x="8" y="26" width="4" height="8" fill="#e21c3d"/><rect x="14" y="20" width="4" height="14" fill="#29a9e1"/><rect x="20" y="16" width="4" height="18" fill="#f47a20"/></svg>
      </div>
    </div>
    <h2 style="background:var(--blue-dark)">Budgeting Service</h2>
    <div class="body"><p>Unlimited consultations to determine holes and waste in spending.</p><p>Client choice from multiple budgeting strategies to determine best personal fit.</p></div>
    <div class="foot" style="background:var(--blue-dark)"></div>
  </section>

  <section class="service" style="left:19px;top:454px">
    <div class="icon-zone" style="background:var(--red)">
      <div class="disc" style="background:#fff;border:8px solid #29a9e1">
        <span style="font-size:40px;font-weight:800;color:#111">$</span>
      </div>
    </div>
    <h2 style="background:var(--red-dark)">Bright Ledger's<br>Credit-Ed Service</h2>
    <div class="body"><p>Personalized assessment with all three bureaus All documentation provided for future use and personal records.</p><p>Provide tools, knowledge, and strategy to prevent future missteps.</p></div>
    <div class="foot" style="background:var(--red-dark)"></div>
  </section>

  <section class="service" style="left:202px;top:454px">
    <div class="icon-zone" style="background:var(--orange)">
      <div class="disc" style="background:#9b3a0c">
        <svg width="44" height="44" viewBox="0 0 44 44"><polyline points="6,38 18,24 26,30 38,12" fill="none" stroke="#fff" stroke-width="4"/><polygon points="32,8 42,6 40,16" fill="#fff"/></svg>
      </div>
    </div>
    <h2 style="background:var(--orange-dark)">Asset Advocate</h2>
    <div class="body" style="text-align:left"><p>Complimentary Rental and Mortgage Assessment</p><p>Quarterly Insurance Assessment</p><p>Quarterly Utility Assessment</p></div>
    <div class="foot" style="background:var(--orange-dark)"></div>
  </section>

  <section class="service" style="left:384px;top:454px">
    <div class="icon-zone" style="background:var(--sky)">
      <div class="disc" style="background:#1b80b8">
        <svg width="36" height="42" viewBox="0 0 36 42"><rect x="3" y="2" width="30" height="38" rx="2" fill="#fff"/><text x="18" y="15" text-anchor="middle" font-family="Mulish,sans-serif" font-size="10" font-weight="800" fill="#123">TAX</text><polyline points="8,23 11,26 16,20" fill="none" stroke="#2db36c" stroke-width="2"/><polyline points="8,32 11,35 16,29" fill="none" stroke="#2db36c" stroke-width="2"/><line x1="19" y1="24" x2="28" y2="24" stroke="#999" stroke-width="2"/><line x1="19" y1="33" x2="28" y2="33" stroke="#999" stroke-width="2"/></svg>
      </div>
    </div>
    <h2 style="background:var(--sky-dark)">Tax Preparation</h2>
    <div class="body"><p>Free prior year return review and amendment filing.</p><p>Guarantee best price</p><p>Partnership discount applied with all future filings.</p></div>
    <div class="foot" style="background:var(--sky-dark)"></div>
  </section>

  <div class="brand"><span class="dot"></span>BRIGHT LEDGER<br>HUB</div>

  <div class="promise">
    <div class="seal-room"></div>
    <p>We provide a FREE CONSULTATION and conduct a full assessment before we take on any new client. Therefore, prospective clients find out upfront if we can actually help them. We pride ourselves on being good corporate citizens as well. For every new household we sign, we commit to providing free service to household below the poverty line.</p>
    <p>Our promise is that we won't take on or charge a client a single cent unless we are ABSOLUTELY SURE we can add value. Our company is fundamentally built upon the service and the help we provide. So if we can't help you, we won't charge you. PERIOD.</p>
  </div>

  <svg class="seal" width="170" height="170" viewBox="0 0 170 170" role="img" aria-label="Satisfaction guarantee seal with ribbon">
    <circle cx="85" cy="85" r="80" fill="#f0b62b"/>
    <circle cx="85" cy="85" r="64" fill="#fbe3a6"/>
  </svg>

  <div class="perks">Starbursts: IN-PERSON BUDGET BUDDY SERVICE,&nbsp; SAVINGS BUILDER,&nbsp; COUPON COMPANION,&nbsp; FREE VIP SEMINAR ACCESS, and more!!!</div>

  <div class="stripe bottom">
    <span style="width:156px;background:var(--green)"></span><span style="width:162px;background:var(--orange)"></span>
    <span style="width:160px;background:var(--red)"></span><span style="width:136px;background:var(--blue)"></span>
    <span style="width:158px;background:var(--green)"></span><span style="width:160px;background:var(--orange)"></span>
    <span style="width:162px;background:var(--red)"></span><span style="width:106px;background:var(--blue)"></span>
  </div>
</div>
</body>
</html>
```